Labels for Hair care products
Labels for hair care products
Project: Labels for Hair care products
Labels for Hair care products  - Salon & Spa
Creative Brief
im looking for new label designs for my hair products i will supply my logo,artwork from my pervious labels and descriptions for each product company name is: QR Scalp Works product line name is called: Grit Rebel
Salon & Spa
lets make it rough and tough looking my demographic target is age 8-30
please make sure i can edit the text, send me all files you use for each label so that i don't have any errors when opening into adobe illustrator. lets keep it about 4 to 5 color max make sure that each label clearly shows that its Shampoo, conditioner, etc

```html
<!DOCTYPE html>
<html lang="en">
<head>
<meta charset="utf-8">
<title>Grit Rebel – Label Set</title>
<link href="https://fonts.googleapis.com/css2?family=Anton&family=Oswald:wght@400;600;700&display=swap" rel="stylesheet">
<style>
  :root{
    --paper:#ffffff;
    --ink-light:#f2f2f2;
    --ink-soft:#c9ccd0;
    --navy:#152b3b;
    --maroon:#3d1212;
    --forest:#0e3b16;
    --blue:#2b9fd9;
    --orange:#e8621d;
    --green:#3aa93c;
    --logo-lime:#a5c93a;
  }
  html,body{margin:0;padding:0;overflow:hidden;background:var(--paper);}
  .sheet{position:relative;width:1200px;height:847px;background:var(--paper);overflow:hidden;font-family:"Oswald",sans-serif;}
  .label{position:absolute;left:144px;width:924px;height:192px;overflow:hidden;background:var(--band);}
  .label--pomade{top:151px;--band:var(--navy);--accent:var(--blue);}
  .label--putty{top:360px;--band:var(--maroon);--accent:var(--orange);}
  .label--gel{top:566px;--band:var(--forest);--accent:var(--green);}

  .copy{position:absolute;left:72px;top:16px;width:200px;color:var(--ink-soft);font-size:7px;line-height:1.35;}
  .copy p{margin:0 0 9px;}
  .copy strong{color:var(--ink-light);font-weight:700;}

  .brand{position:absolute;display:flex;align-items:center;gap:4px;color:var(--logo-lime);font-weight:600;font-size:10px;letter-spacing:.3px;white-space:nowrap;}
  .brand::before{content:"";width:8px;height:8px;background:var(--logo-lime);}
  .brand--foot{left:72px;top:152px;}
  .brand--head{left:400px;top:17px;}
  .distributor{position:absolute;left:172px;top:148px;width:130px;color:var(--ink-soft);font-size:7px;line-height:1.3;}
  .distributor strong{color:var(--ink-light);}

  .origin,.weight{position:absolute;top:100px;color:var(--ink-light);font-size:9px;font-weight:600;letter-spacing:.3px;white-space:nowrap;}
  .origin{left:396px;}
  .weight{left:804px;}

  .burst{position:absolute;left:640px;top:-20px;width:190px;height:190px;border-radius:50%;
    background:radial-gradient(circle,var(--accent) 0%,color-mix(in srgb,var(--accent) 40%,transparent) 45%,transparent 70%);opacity:.85;}

  .product-type{position:absolute;left:540px;top:36px;color:var(--ink-light);font-weight:700;font-size:15px;letter-spacing:.4px;white-space:nowrap;}
  .product-name{position:absolute;left:538px;top:56px;color:var(--ink-light);font-family:"Anton",sans-serif;font-size:48px;line-height:1;letter-spacing:1px;text-transform:uppercase;white-space:nowrap;}
  .ribbon{position:absolute;left:510px;top:118px;width:284px;height:28px;}
  .tagline{position:absolute;left:540px;top:120px;color:var(--ink-light);font-weight:700;font-size:15px;letter-spacing:.4px;white-space:nowrap;}
  .audience{position:absolute;left:540px;top:150px;color:var(--accent);font-weight:600;font-size:10px;letter-spacing:.3px;white-space:nowrap;}
</style>
</head>
<body>
<main class="sheet">

  <section class="label label--pomade">
    <div class="copy">
      <p>Shape, hold and finish any style with a firm grip that lasts all day and rinses out clean.</p>
      <p><strong>DIRECTIONS:</strong> Warm a small amount between palms and work through damp or dry hair. Style as desired.</p>
      <p><strong>INGREDIENTS:</strong> Water, beeswax, lanolin, castor oil, glycerin, fragrance, panthenol, vitamin E, citric acid.</p>
    </div>
    <div class="brand brand--foot">QR Scalp Works</div>
    <div class="distributor"><strong>DISTRIBUTED BY:</strong> QR Scalp Works 210 Example Road Springfield USA</div>
    <div class="brand brand--head">QR Scalp Works</div>
    <div class="origin">MADE IN USA</div>
    <div class="burst" role="img" aria-label="Blue radiating burst decoration"></div>
    <div class="product-type">IRON GRIP POMADE</div>
    <div class="product-name">Grit Rebel</div>
    <svg class="ribbon" viewBox="0 0 284 28"><polygon points="0,4 276,0 284,24 8,28" fill="var(--accent)"/></svg>
    <div class="tagline">PRO HOLD, NO CHAIR NEEDED</div>
    <div class="audience">FOR MEN AND WOMEN</div>
    <div class="weight">4 OZ 114 GRAMS</div>
  </section>

  <section class="label label--putty">
    <div class="copy">
      <p>Shape, hold and finish any style with a firm grip that lasts all day and rinses out clean.</p>
      <p><strong>DIRECTIONS:</strong> Warm a small amount between palms and work through damp or dry hair. Style as desired.</p>
      <p><strong>INGREDIENTS:</strong> Water, beeswax, lanolin, castor oil, glycerin, fragrance, panthenol, vitamin E, citric acid.</p>
    </div>
    <div class="brand brand--foot">QR Scalp Works</div>
    <div class="distributor"><strong>DISTRIBUTED BY:</strong> QR Scalp Works 210 Example Road Springfield USA</div>
    <div class="brand brand--head">QR Scalp Works</div>
    <div class="origin">MADE IN USA</div>
    <div class="burst" role="img" aria-label="Orange radiating burst decoration"></div>
    <div class="product-type">SCULPT CLAY</div>
    <div class="product-name">Grit Rebel</div>
    <svg class="ribbon" viewBox="0 0 284 28"><polygon points="0,4 276,0 284,24 8,28" fill="var(--accent)"/></svg>
    <div class="tagline">PRO HOLD, NO CHAIR NEEDED</div>
    <div class="audience">FOR MEN AND WOMEN</div>
    <div class="weight">4 OZ 114 GRAMS</div>
  </section>

  <section class="label label--gel">
    <div class="copy">
      <p>Shape, hold and finish any style with a firm grip that lasts all day and rinses out clean.</p>
      <p><strong>DIRECTIONS:</strong> Warm a small amount between palms and work through damp or dry hair. Style as desired.</p>
      <p><strong>INGREDIENTS:</strong> Water, beeswax, lanolin, castor oil, glycerin, fragrance, panthenol, vitamin E, citric acid.</p>
    </div>
    <div class="brand brand--foot">QR Scalp Works</div>
    <div class="distributor"><strong>DISTRIBUTED BY:</strong> QR Scalp Works 210 Example Road Springfield USA</div>
    <div class="brand brand--head">QR Scalp Works</div>
    <div class="origin">MADE IN USA</div>
    <div class="burst" role="img" aria-label="Green radiating burst decoration"></div>
    <div class="product-type">STONE SET HAIR GEL</div>
    <div class="product-name">Grit Rebel</div>
    <svg class="ribbon" viewBox="0 0 284 28"><polygon points="0,4 276,0 284,24 8,28" fill="var(--accent)"/></svg>
    <div class="tagline">PRO HOLD, NO CHAIR NEEDED</div>
    <div class="audience">FOR MEN AND WOMEN</div>
    <div class="weight">4 OZ 114 GRAMS</div>
  </section>

</main>
</body>
</html>
```